Graphic Design Project

We are currently undertaking a new business venture. We have developed a business strategy which we wish to present to our prospective business partner as a one page visual.
The business strategy which we developed is in word format. We would like to be able to present our partner with a chart that is more professional visually.
Ideally we would like to be able to edit the document, so that as the strategy changes we can update it - but this is not essential if it hinders the design. Please let us know what format you will be providing the document in.
I have attached a copy of the chart that we created. When we pick the successful design we will send you our company name and logo be included in the design.
Target Market(s)
We are a training company and our new business venture is with another training and development company
Industry/Entity Type
Business
Requirements
Nice to have
- Editable version

```html
<!DOCTYPE html>
<html lang="en">
<head>
<meta charset="utf-8">
<title>Business Strategy Chart</title>
<link rel="stylesheet" href="https://fonts.googleapis.com/css2?family=Jost:wght@300;400;500&family=Gelasio:ital,wght@1,500&display=swap">
<style>
  :root {
    --page-bg: #f7d08c;
    --frame: #66bb00;
    --logo-green: #7cc43a;
    --note-paper: #ffffff;
    --note-fill: #ccf5a6;
    --note-dash: #a9d98a;
    --ink: #1c1c1c;
    --ink-soft: #3a3a3a;
    --stage-top: #8fd15a;
    --stage-bottom: #6ca23a;
    --stage-edge: #e8f0dc;
    --arrow-light: #8fe02a;
    --arrow-dark: #4fa000;
  }
  * { box-sizing: border-box; margin: 0; padding: 0; }
  html, body { width: 1200px; height: 1095px; overflow: hidden; background: var(--page-bg); }
  .canvas {
    position: relative; width: 1200px; height: 1095px;
    background: var(--page-bg); border: 4px solid var(--frame);
  }
  .brand {
    position: absolute; left: 312px; top: 44px; width: 446px;
    text-align: center; font-family: "Jost", sans-serif; font-weight: 300;
    font-size: 50px; letter-spacing: 1px; color: var(--logo-green); line-height: 60px;
  }
  .brand-rule {
    position: absolute; left: 312px; top: 106px; width: 446px; height: 2px;
    background: linear-gradient(90deg, rgba(255,255,255,.9), rgba(255,255,255,.9) 60%, rgba(255,255,255,.2));
  }
  .note {
    position: absolute; width: 170px; padding: 6px;
    background: var(--note-paper);
    box-shadow: 0 6px 6px -3px rgba(0,0,0,.35);
  }
  .note-body {
    background: var(--note-fill); border: 1px dashed var(--note-dash);
    padding: 8px 0 7px 14px; height: 100%;
  }
  .note-title {
    font-family: "Jost", sans-serif; font-weight: 400; font-size: 18px;
    color: var(--ink); line-height: 24px; margin-bottom: 3px; margin-left: -2px;
  }
  .note-line, .stage-line {
    font-family: "Gelasio", serif; font-style: italic; font-weight: 500;
    font-size: 12.5px; line-height: 18.8px;
  }
  .note-line { color: var(--ink-soft); }
  .note.tall { height: 172px; }
  .note.short { height: 115px; }
  .stage {
    position: absolute; top: 402px; width: 171px; height: 129px;
    background: linear-gradient(180deg, var(--stage-top), var(--stage-bottom));
    border: 2px solid var(--stage-edge); border-radius: 5px;
    box-shadow: 0 2px 6px rgba(0,0,0,.3);
    padding: 8px 0 0 16px;
  }
  .stage-title {
    font-family: "Jost", sans-serif; font-weight: 400; font-size: 20px;
    color: #fff; text-align: center; margin-left: -16px; line-height: 26px; margin-bottom: 4px;
  }
  .stage-line { color: #fff; }
  .connectors { position: absolute; left: -4px; top: -4px; width: 1200px; height: 1095px; pointer-events: none; }
</style>
</head>
<body>
<div class="canvas">
  <div class="brand">COMPANY LOGO</div>
  <div class="brand-rule"></div>

  <!-- Inputs row -->
  <div class="note tall" style="left:87px;top:165px"><div class="note-body"><p class="note-title">Title Goes Here</p><p class="note-line">Lorem ipsum dolor sit</p><p class="note-line">Lorem ipsum dolor sit</p><p class="note-line">Lorem ipsum dolor sit</p><p class="note-line">Lorem ipsum dolor sit</p><p class="note-line">Lorem ipsum dolor sit</p><p class="note-line">Lorem ipsum dolor sit</p></div></div>
  <div class="note tall" style="left:306px;top:165px"><div class="note-body"><p class="note-title">Title Goes Here</p><p class="note-line">Lorem ipsum dolor sit</p><p class="note-line">Lorem ipsum dolor sit</p><p class="note-line">Lorem ipsum dolor sit</p><p class="note-line">Lorem ipsum dolor sit</p><p class="note-line">Lorem ipsum dolor sit</p><p class="note-line">Lorem ipsum dolor sit</p></div></div>
  <div class="note tall" style="left:526px;top:165px"><div class="note-body"><p class="note-title">Title Goes Here</p><p class="note-line">Lorem ipsum dolor sit</p><p class="note-line">Lorem ipsum dolor sit</p><p class="note-line">Lorem ipsum dolor sit</p><p class="note-line">Lorem ipsum dolor sit</p><p class="note-line">Lorem ipsum dolor sit</p><p class="note-line">Lorem ipsum dolor sit</p></div></div>
  <div class="note tall" style="left:745px;top:165px"><div class="note-body"><p class="note-title">Title Goes Here</p><p class="note-line">Lorem ipsum dolor sit</p><p class="note-line">Lorem ipsum dolor sit</p><p class="note-line">Lorem ipsum dolor sit</p><p class="note-line">Lorem ipsum dolor sit</p><p class="note-line">Lorem ipsum dolor sit</p><p class="note-line">Lorem ipsum dolor sit</p></div></div>
  <div class="note tall" style="left:965px;top:165px"><div class="note-body"><p class="note-title">Title Goes Here</p><p class="note-line">Lorem ipsum dolor sit</p><p class="note-line">Lorem ipsum dolor sit</p><p class="note-line">Lorem ipsum dolor sit</p><p class="note-line">Lorem ipsum dolor sit</p><p class="note-line">Lorem ipsum dolor sit</p><p class="note-line">Lorem ipsum dolor sit</p></div></div>

  <!-- Stages row -->
  <div class="stage" style="left:82px"><p class="stage-title">Title Here</p><p class="stage-line">Lorem ipsum dolor sit</p><p class="stage-line">Lorem ipsum dolor sit</p><p class="stage-line">Lorem ipsum dolor sit</p><p class="stage-line">Lorem ipsum dolor sit</p></div>
  <div class="stage" style="left:302px"><p class="stage-title">Title Here</p><p class="stage-line">Lorem ipsum dolor sit</p><p class="stage-line">Lorem ipsum dolor sit</p><p class="stage-line">Lorem ipsum dolor sit</p><p class="stage-line">Lorem ipsum dolor sit</p></div>
  <div class="stage" style="left:522px"><p class="stage-title">Title Here</p><p class="stage-line">Lorem ipsum dolor sit</p><p class="stage-line">Lorem ipsum dolor sit</p><p class="stage-line">Lorem ipsum dolor sit</p><p class="stage-line">Lorem ipsum dolor sit</p></div>
  <div class="stage" style="left:741px"><p class="stage-title">Title Here</p><p class="stage-line">Lorem ipsum dolor sit</p><p class="stage-line">Lorem ipsum dolor sit</p><p class="stage-line">Lorem ipsum dolor sit</p><p class="stage-line">Lorem ipsum dolor sit</p></div>
  <div class="stage" style="left:960px"><p class="stage-title">Title Here</p><p class="stage-line">Lorem ipsum dolor sit</p><p class="stage-line">Lorem ipsum dolor sit</p><p class="stage-line">Lorem ipsum dolor sit</p><p class="stage-line">Lorem ipsum dolor sit</p></div>

  <!-- Supporting notes below -->
  <div class="note tall" style="left:83px;top:585px"><div class="note-body"><p class="note-title">Title Goes Here</p><p class="note-line">Lorem ipsum dolor sit</p><p class="note-line">Lorem ipsum dolor sit</p><p class="note-line">Lorem ipsum dolor sit</p><p class="note-line">Lorem ipsum dolor sit</p><p class="note-line">Lorem ipsum dolor sit</p><p class="note-line">Lorem ipsum dolor sit</p></div></div>
  <div class="note tall" style="left:294px;top:585px"><div class="note-body"><p class="note-title">Title Goes Here</p><p class="note-line">Lorem ipsum dolor sit</p><p class="note-line">Lorem ipsum dolor sit</p><p class="note-line">Lorem ipsum dolor sit</p><p class="note-line">Lorem ipsum dolor sit</p><p class="note-line">Lorem ipsum dolor sit</p><p class="note-line">Lorem ipsum dolor sit</p></div></div>
  <div class="note short" style="left:294px;top:791px"><div class="note-body"><p class="note-title">Title Goes Here</p><p class="note-line">Lorem ipsum dolor sit</p><p class="note-line">Lorem ipsum dolor sit</p><p class="note-line">Lorem ipsum dolor sit</p></div></div>
  <div class="note short" style="left:294px;top:935px"><div class="note-body"><p class="note-title">Title Goes Here</p><p class="note-line">Lorem ipsum dolor sit</p><p class="note-line">Lorem ipsum dolor sit</p><p class="note-line">Lorem ipsum dolor sit</p></div></div>
  <div class="note tall" style="left:522px;top:585px"><div class="note-body"><p class="note-title">Title Goes Here</p><p class="note-line">Lorem ipsum dolor sit</p><p class="note-line">Lorem ipsum dolor sit</p><p class="note-line">Lorem ipsum dolor sit</p><p class="note-line">Lorem ipsum dolor sit</p><p class="note-line">Lorem ipsum dolor sit</p><p class="note-line">Lorem ipsum dolor sit</p></div></div>
  <div class="note tall" style="left:857px;top:585px"><div class="note-body"><p class="note-title">Title Goes Here</p><p class="note-line">Lorem ipsum dolor sit</p><p class="note-line">Lorem ipsum dolor sit</p><p class="note-line">Lorem ipsum dolor sit</p><p class="note-line">Lorem ipsum dolor sit</p><p class="note-line">Lorem ipsum dolor sit</p><p class="note-line">Lorem ipsum dolor sit</p></div></div>
  <div class="note tall" style="left:857px;top:794px"><div class="note-body"><p class="note-title">Title Goes Here</p><p class="note-line">Lorem ipsum dolor sit</p><p class="note-line">Lorem ipsum dolor sit</p><p class="note-line">Lorem ipsum dolor sit</p><p class="note-line">Lorem ipsum dolor sit</p><p class="note-line">Lorem ipsum dolor sit</p><p class="note-line">Lorem ipsum dolor sit</p></div></div>

  <svg class="connectors" viewBox="0 0 1200 1095" aria-hidden="true">
    <defs>
      <linearGradient id="arrowFill" x1="0" y1="0" x2="0" y2="1">
        <stop offset="0" stop-color="var(--arrow-light)"/>
        <stop offset="1" stop-color="var(--arrow-dark)"/>
      </linearGradient>
      <polygon id="chevDown" points="-17,-14 0,0 17,-14 17,-2 0,14 -17,-2" fill="url(#arrowFill)"/>
      <polygon id="chevUp" points="-17,14 0,0 17,14 17,2 0,-14 -17,2" fill="url(#arrowFill)"/>
      <polygon id="chevRight" points="-14,-17 0,0 -14,17 -2,17 14,0 -2,-17" fill="url(#arrowFill)"/>
      <g id="pin"><line x1="-4" y1="-8" x2="1" y2="0" stroke="#222" stroke-width="1.3"/><circle cx="1" cy="1" r="1.6" fill="#222"/></g>
    </defs>

    <use href="#chevDown" x="176" y="374"/>
    <use href="#chevDown" x="395" y="374"/>
    <use href="#chevDown" x="615" y="374"/>
    <use href="#chevDown" x="834" y="374"/>
    <use href="#chevDown" x="1054" y="374"/>

    <use href="#chevRight" x="284" y="468"/>
    <use href="#chevRight" x="503" y="468"/>
    <use href="#chevRight" x="727" y="465"/>
    <use href="#chevRight" x="944" y="461"/>

    <use href="#chevUp" x="172" y="561"/>
    <use href="#chevUp" x="380" y="561"/>
    <use href="#chevUp" x="608" y="561"/>
    <use href="#chevUp" x="892" y="561" transform="rotate(-18 892 561)"/>
    <use href="#chevUp" x="982" y="561" transform="rotate(18 982 561)"/>
    <use href="#chevUp" x="380" y="778"/>
    <use href="#chevUp" x="380" y="920"/>
    <use href="#chevUp" x="945" y="776"/>

    <use href="#pin" x="176" y="171"/>
    <use href="#pin" x="395" y="171"/>
    <use href="#pin" x="615" y="171"/>
    <use href="#pin" x="834" y="171"/>
    <use href="#pin" x="1054" y="171"/>
    <use href="#pin" x="172" y="591"/>
    <use href="#pin" x="383" y="591"/>
    <use href="#pin" x="611" y="591"/>
    <use href="#pin" x="946" y="591"/>
    <use href="#pin" x="383" y="797"/>
    <use href="#pin" x="383" y="941"/>
    <use href="#pin" x="946" y="800"/>
  </svg>
</div>
</body>
</html>
```